Business cards for financial advisor-insurance agent firm

Our company, Harlow Pemberton Insurance & Investments, is an insurance (health, life, home, auto, etc) and investment brokerage offering a suite of options to meet client needs. We need business cards that are professional and embody strength, security and sophistication.

Also running a letterhead project at
http://jobs.briefmarlo.com/job.aspx?id=519087

Target Market(s)

Upper middle class and wealthy

Industry/Entity Type

Investment

Requirements
Nice to have
• Looking for either white, navy blue, or gray cards

```html
<!DOCTYPE html>
<html lang="en">
<head>
<meta charset="utf-8">
<title>Harlow Pemberton Insurance &amp; Investments — Business Card</title>
<link rel="stylesheet" href="https://fonts.googleapis.com/css2?family=Arimo:wght@400&display=swap">
<style>
  :root {
    --navy: #2a3566;
    --paper: #f7f7f5;
    --backdrop: #dcdcd6;
    --pattern-light: #ecedeb;
    --pattern-navy: #2f3b6f;
    --ink-light: #ffffff;
    --ink-muted: #c9cde0;
    --rule: #6d77a3;
  }
  * { margin: 0; padding: 0; box-sizing: border-box; }
  html, body { width: 1000px; height: 1200px; overflow: hidden; }
  body {
    background: var(--backdrop);
    position: relative;
    font-family: "Arimo", sans-serif;
  }
  .card {
    position: absolute;
    left: 150px;
    width: 700px;
    height: 400px;
    overflow: hidden;
    box-shadow: 0 10px 30px rgba(0,0,0,0.12);
  }
  .card--front { top: 150px; background: var(--paper); }
  .card--back  { top: 650px; background: var(--navy); }

  .pattern {
    position: absolute;
    width: 360px;
    height: 360px;
    transform: rotate(45deg);
  }
  .card--front .pattern { left: 170px; top: 20px; background: var(--pattern-light); }
  .card--back .pattern  { left: -20px; top: -200px; background: var(--pattern-navy); }

  .company {
    position: absolute;
    display: flex;
    flex-direction: column;
    align-items: center;
    font-weight: 400;
  }
  .company__name { font-size: 32px; line-height: 1; }
  .company__line { font-size: 14px; margin-top: 8px; }
  .card--front .company { color: var(--navy); left: 0; right: 0; top: 170px; }
  .card--back .company  { color: var(--ink-light); left: 60px; top: 70px; }
  .card--back .company__name { font-size: 22px; }
  .card--back .company__line { font-size: 11px; margin-top: 6px; }

  .contact {
    position: absolute;
    left: 380px;
    top: 205px;
    width: 280px;
    color: var(--ink-light);
  }
  .contact__name { font-size: 26px; line-height: 1.1; }
  .contact__role { font-size: 13px; color: var(--ink-muted); margin-top: 2px; }
  .contact__rule { height: 1px; background: var(--rule); margin: 12px 0 10px; }
  .contact__list { list-style: none; }
  .contact__item {
    display: flex; align-items: center; gap: 8px;
    font-size: 12px; color: var(--ink-muted); line-height: 22px;
  }
  .contact__icon { width: 12px; height: 12px; fill: var(--ink-light); flex: none; }
</style>
</head>
<body>

  <section class="card card--front" aria-label="Business card front">
    <div class="pattern" role="img" aria-label="Faint nested square frame pattern"></div>
    <div class="company">
      <span class="company__name">Harlow Pemberton</span>
      <span class="company__line">Insurance &amp; Investments</span>
    </div>
  </section>

  <section class="card card--back" aria-label="Business card back">
    <div class="pattern" role="img" aria-label="Tone-on-tone nested square frame pattern"></div>
    <div class="company">
      <span class="company__name">Harlow Pemberton</span>
      <span class="company__line">Insurance &amp; Investments</span>
    </div>

    <div class="contact">
      <div class="contact__name">Miles Ashworth</div>
      <div class="contact__role">Manager</div>
      <div class="contact__rule"></div>
      <ul class="contact__list">
        <li class="contact__item">
          <svg class="contact__icon" viewBox="0 0 12 12"><path d="M6 0a4 4 0 0 0-4 4c0 3 4 8 4 8s4-5 4-8a4 4 0 0 0-4-4zm0 5.5A1.5 1.5 0 1 1 6 2.5a1.5 1.5 0 0 1 0 3z"/></svg>
          your address
        </li>
        <li class="contact__item">
          <svg class="contact__icon" viewBox="0 0 12 12"><path d="M2.5 0.5l2 2.5-1.2 1.4a7 7 0 0 0 4.3 4.3L9 7.5l2.5 2-1 2C5 11.5 0.5 7 0.5 1.5z"/></svg>
          010 24137 5962
        </li>
        <li class="contact__item">
          <svg class="contact__icon" viewBox="0 0 12 12"><path d="M6 0a6 6 0 1 0 0 12A6 6 0 0 0 6 0zm0 1.2c.8 0 1.6 1.8 1.8 4.2H4.2C4.4 3 5.2 1.2 6 1.2zM4.2 6.6h3.6C7.6 9 6.8 10.8 6 10.8S4.4 9 4.2 6.6zM1.2 6.6H3c.1 1.5.4 2.8.9 3.7a4.8 4.8 0 0 1-2.7-3.7zm0-1.2a4.8 4.8 0 0 1 2.7-3.7C3.4 2.6 3.1 3.9 3 5.4zm7.8 0c-.1-1.5-.4-2.8-.9-3.7a4.8 4.8 0 0 1 2.7 3.7zm0 1.2h1.8a4.8 4.8 0 0 1-2.7 3.7c.5-.9.8-2.2.9-3.7z"/></svg>
          www.harlowpemberton.com
        </li>
        <li class="contact__item">
          <svg class="contact__icon" viewBox="0 0 12 12"><path d="M0 2h12v8H0zm1.2 1.2v.4L6 6.8l4.8-3.2v-.4zm0 1.8v3.8h9.6V5L6 8.2z"/></svg>
          name@harlowpemberton.com
        </li>
      </ul>
    </div>
  </section>

</body>
</html>
```